Ward Compass Business Card Design*

We need a business card design for our company Ward Compass. Our company is specialized in providing online consulting services regarding medical institutions, hospitals and doctors. We work with patients worldwide looking to choose between healthcare providers. We have a website you may use as a reference, where we list doctors and clinics worldwide. So we target Medical providers as well as patients worldwide.
Target Market(s)
Medical Providers and patients around the world
Industry/Entity Type
Medical
Contact Information for Business Card
Salma Derkaoui
CEO
+90 612 348 2071
info@wardcompass-example.com
www.wardcompass-example.com
14 Annakhil 3 H.R.B. Rabat, Morocco
Requirements
Must have
- Company logo/name on one full side, personal info and smaller logo and company name on the other side.
Nice to have
- Smart and elegant design

```html
<!DOCTYPE html>
<html lang="en">
<head>
<meta charset="utf-8">
<title>Ward Compass Business Card</title>
<link href="https://fonts.googleapis.com/css2?family=Lato:wght@400;700;900&display=swap" rel="stylesheet">
<style>
  :root {
    --navy: #133767;
    --grey: #808083;
    --white: #ffffff;
    --ink: #2b2b2b;
    --backdrop: #d9d9d7;
  }
  * { box-sizing: border-box; margin: 0; padding: 0; }
  html, body { width: 1200px; height: 801px; overflow: hidden; }
  body {
    background: var(--backdrop);
    font-family: "Lato", sans-serif;
    position: relative;
  }
  .card {
    position: absolute;
    top: 245px;
    width: 540px;
    height: 310px;
    background: var(--white);
    overflow: hidden;
    box-shadow: 0 6px 18px rgba(0,0,0,0.18);
  }
  .card--front { left: 40px; }
  .card--back { left: 620px; }
  .card__waves { position: absolute; inset: 0; }
  .brand {
    position: absolute;
    display: flex;
    align-items: center;
    gap: 12px;
    color: var(--navy);
    font-weight: 700;
    text-transform: uppercase;
    letter-spacing: 1px;
    white-space: nowrap;
  }
  .brand__dot {
    border-radius: 50%;
    background: var(--navy);
    flex: none;
  }
  .card--front .brand { left: 30px; top: 96px; font-size: 21px; gap: 10px; }
  .card--front .brand__dot { width: 34px; height: 34px; }
  .card--back .brand { left: 50%; top: 108px; transform: translateX(-50%); font-size: 36px; gap: 16px; }
  .card--back .brand__dot { width: 56px; height: 56px; }
  .person {
    position: absolute;
    left: 352px;
    top: 128px;
    color: var(--white);
  }
  .person__name { font-size: 16px; font-weight: 900; }
  .person__role { font-size: 11.5px; margin-top: 2px; }
  .contacts {
    list-style: none;
    margin-top: 14px;
    font-size: 10.5px;
    line-height: 1.6;
  }
  .contacts li { display: flex; align-items: center; gap: 7px; white-space: nowrap; }
  .contacts svg { width: 10px; height: 10px; flex: none; }
  .address {
    position: absolute;
    left: 30px;
    bottom: 18px;
    color: var(--white);
    font-size: 13px;
    line-height: 1.35;
  }
  .website {
    position: absolute;
    left: 0; right: 0;
    top: 222px;
    text-align: center;
    color: var(--ink);
    font-size: 15px;
    letter-spacing: 0.5px;
  }
</style>
</head>
<body>
  <section class="card card--front">
    <svg class="card__waves" viewBox="0 0 540 310" aria-hidden="true">
      <path d="M0,222 C160,214 260,180 315,112 C365,44 410,8 470,0 L540,0 L540,310 L0,310 Z" fill="var(--grey)"/>
      <path d="M0,242 C170,234 282,200 337,128 C387,56 430,16 488,0 L540,0 L540,310 L0,310 Z" fill="var(--white)"/>
      <path d="M0,246 C172,238 286,204 341,132 C391,60 434,20 492,0 L540,0 L540,310 L0,310 Z" fill="var(--navy)"/>
    </svg>
    <div class="brand"><span class="brand__dot"></span>Ward Compass</div>
    <div class="person">
      <p class="person__name">Salma Derkaoui</p>
      <p class="person__role">CEO</p>
      <ul class="contacts">
        <li>
          <svg viewBox="0 0 12 12" aria-hidden="true"><path d="M2.5 1 L4.5 1 L5.2 3.6 L4 4.6 C4.6 6 5.9 7.4 7.4 8 L8.4 6.8 L11 7.5 L11 9.5 C11 10.3 10.3 11 9.5 11 C5 11 1 7 1 2.5 C1 1.7 1.7 1 2.5 1 Z" fill="var(--white)"/></svg>
          +90 612 348 2071
        </li>
        <li>
          <svg viewBox="0 0 12 12" aria-hidden="true"><rect x="0.5" y="2" width="11" height="8" fill="var(--white)"/><path d="M0.8 2.4 L6 6.6 L11.2 2.4" fill="none" stroke="var(--navy)" stroke-width="1"/></svg>
          info@wardcompass-example.com
        </li>
        <li>
          <svg viewBox="0 0 12 12" aria-hidden="true"><circle cx="6" cy="6" r="5.3" fill="var(--white)"/><path d="M0.8 6 H11.2 M6 0.8 V11.2 M6 0.8 C3.5 3.5 3.5 8.5 6 11.2 M6 0.8 C8.5 3.5 8.5 8.5 6 11.2" fill="none" stroke="var(--navy)" stroke-width="0.7"/></svg>
          www.wardcompass-example.com
        </li>
      </ul>
    </div>
    <p class="address">14 Annakhil 3<br>H.R.B. Rabat, Morocco</p>
  </section>

  <section class="card card--back">
    <div class="brand"><span class="brand__dot"></span>Ward Compass</div>
    <p class="website">www.wardcompass-example.com</p>
  </section>
</body>
</html>
```